Corvella wealth client piece

I would like a high end Client brochere for Corvella wealth advisors

Target Market(s)

Investors who want to align their faith and their investments

Industry/Entity Type

Finance

Font styles to use
Serif

Colors
0054AA
0677BA
7BADD7
CADEEF
E8F1F8

Requirements
Must have
• It must reference our “trust and ledger index “. A tool we developed to help people see. What their investments are supporting
Nice to have
• Images etc from our web site www.Corvella wealth.com
Should not have
• No negative or judgmental language

```html
<!DOCTYPE html>
<html lang="en">
<head>
<meta charset="utf-8">
<title>Corvella Wealth Advisors – Client Brochure</title>
<link href="https://fonts.googleapis.com/css2?family=Lora:wght@400;500;600;700&display=swap" rel="stylesheet">
<style>
:root{
  --brand-blue:#0054AA;
  --mid-blue:#0677BA;
  --sky-blue:#7BADD7;
  --pale-blue:#CADEEF;
  --mist-blue:#E8F1F8;
  --navy:#17497c;
  --ink:#1d2a3a;
  --grey-panel:#eeeff0;
  --canvas:#f3f3f3;
  --white:#ffffff;
}
*{box-sizing:border-box;margin:0;padding:0}
html,body{width:1200px;height:3000px;overflow:hidden}
body{background:var(--canvas);font-family:"Lora",serif;color:var(--ink);position:relative}
.spread{position:absolute;left:40px;width:1120px;height:725px;background:var(--white);overflow:hidden;box-shadow:0 2px 10px rgba(0,0,0,.12)}
.spread--outer{top:735px}
.spread--inner{top:1540px}
.abs{position:absolute}

/* outer spread */
.photo-strip{left:0;top:0;width:168px;height:725px;background:linear-gradient(180deg,#dfe9f3 0%,#9dbcd9 35%,#c7d6e2 60%,#6b6f6c 85%,#3d3f38 100%)}
.about{left:168px;top:0;width:391px;height:725px;text-align:center}
.about__title{top:50px;left:0;width:100%;font-size:20px;font-weight:700;color:var(--navy);letter-spacing:.5px}
.about__text{left:34px;width:323px;font-size:8.6px;line-height:1.45;color:#333}
.about__text--intro{top:88px}
.about__text--close{top:304px}
.callout{left:36px;top:210px;width:320px;height:74px;background:var(--pale-blue);color:var(--brand-blue);font-size:14.5px;font-weight:500;line-height:1.3;display:flex;align-items:center;justify-content:center;padding:0 16px}
.about__rule{left:162px;top:392px;width:66px;height:1px;background:#b9c3cc}
.brand-mark{display:flex;align-items:center;gap:10px;font-weight:600}
.brand-mark__square{width:26px;height:26px;background:currentColor;flex:none}
.about__brand{left:0;top:420px;width:100%;justify-content:center;color:var(--navy);font-size:17px}
.contact__label{top:480px;left:0;width:100%;font-size:22px;font-weight:400;color:#222}
.contact__icons{top:522px;left:0;width:100%;display:flex;justify-content:center;gap:16px}
.contact__icons span{width:36px;height:36px;border-radius:50%;background:#111;display:flex;align-items:center;justify-content:center}
.contact__phone{top:568px;left:0;width:100%;font-size:30px;font-weight:700;color:#111}
.contact__email{top:616px;left:0;width:100%;font-size:11px;font-weight:600;color:#111}
.contact__web{top:640px;left:0;width:100%;font-size:11px;font-weight:600;color:#111}
.contact__social{top:682px;left:0;width:100%;display:flex;justify-content:center;gap:16px}
.contact__social span{width:10px;height:10px;background:var(--navy)}

.cover{left:559px;top:0;width:561px;height:725px;color:var(--white)}
.cover__photo{left:0;top:0;width:561px;height:725px;background:linear-gradient(180deg,#1a5ea6 0%,#2a6fb6 40%,#3f82c3 62%,#a9a493 80%,#d8d0bf 100%)}
.cover__brand{left:58px;top:40px;font-size:24px;color:var(--white)}
.cover__brand .brand-mark__square{width:34px;height:34px}
.cover__line{left:58px;font-weight:700;letter-spacing:.3px;text-transform:uppercase;white-space:nowrap;line-height:1}
.cover__line--1{top:168px;font-size:29px}
.cover__line--2{top:206px;font-size:29px}
.cover__line--3{top:244px;font-size:34px}
.cover__tag{left:58px;top:296px;font-size:11px;font-weight:700;font-variant:small-caps;letter-spacing:.3px}

/* inner spread */
.benefits-band{left:0;top:0;width:559px;height:409px;background:var(--navy)}
.benefits__lead{left:38px;top:34px;width:290px;font-size:17px;font-weight:600;line-height:1.3;color:var(--white);text-transform:uppercase}
.benefits__head{left:38px;top:112px;font-size:26px;font-weight:700;line-height:1.15;color:var(--white);text-transform:uppercase}
.benefits__rule{left:40px;top:222px;width:44px;height:3px;background:var(--white)}
.family-photo{left:34px;top:242px;width:278px;height:468px;background:linear-gradient(160deg,#e9dcc0 0%,#cfb98f 40%,#9c8a66 75%,#6e6446 100%)}
.benefit-list{left:346px;top:36px;width:200px;list-style:none;color:var(--white)}
.benefit-list li{position:absolute;left:0;display:flex;gap:14px;width:200px}
.benefit-list b{font-size:19px;font-weight:700;width:28px;flex:none;line-height:1.1}
.benefit-list span{font-size:10.5px;line-height:1.3;padding-top:3px}
.firm__brand{left:346px;top:426px;font-size:14px;color:var(--pale-blue)}
.firm__brand .brand-mark__square{width:18px;height:18px}
.firm__lead{left:346px;top:464px;width:200px;font-size:13px;font-weight:600;line-height:1.3;color:#111}
.firm__tech{left:346px;top:604px;width:196px;font-size:10.5px;font-weight:600;line-height:1.35;color:var(--brand-blue)}

.steps{left:559px;top:0;width:290px;height:725px}
.step{position:absolute;left:0;width:290px}
.step--index{top:0;height:247px;background:var(--grey-panel)}
.step--account{top:247px;height:262px;background:var(--white)}
.step--progress{top:509px;height:216px;background:var(--grey-panel)}
.step__art{position:absolute;left:34px;width:170px;height:70px;background:linear-gradient(135deg,var(--mist-blue),var(--pale-blue))}
.step__title{position:absolute;left:34px;width:220px;font-size:12px;font-weight:700;color:var(--navy);text-transform:uppercase;line-height:1.3}
.step__text{position:absolute;left:34px;width:210px;font-size:9.5px;line-height:1.4;color:#333}

.baby-photo{left:849px;top:0;width:271px;height:470px;background:linear-gradient(180deg,#2a6cb3 0%,#5f97cf 45%,#b7cfe4 72%,#d9dee2 100%)}
.faq{left:886px;width:210px}
.faq__q{font-size:9.5px;font-weight:700;color:var(--navy);line-height:1.3}
.faq__a{font-size:7.8px;line-height:1.45;color:#333;margin-top:8px}
.faq--cost{top:510px}
.faq--help{top:636px}
</style>
</head>
<body>

<section class="spread spread--outer">
  <div class="abs photo-strip" role="img" aria-label="Photo: silhouette of a father lifting a child toward a bright sky above a field"></div>

  <div class="abs about">
    <h2 class="abs about__title">ABOUT US</h2>
    <p class="abs about__text about__text--intro">Corvella Wealth Advisors℠ draws on a long tradition of thoughtful stewardship, where careful study and steady principles shape every decision. Our advisors bring decades of professional discipline to each client relationship, pairing time-tested values with modern financial insight. Our vision, our craft and our moral clarity sit at the core of our firm's identity and purpose.</p>
    <div class="abs callout">At Corvella Wealth Advisors℠, we believe that good returns and good values are not mutually exclusive.</div>
    <p class="abs about__text about__text--close">We strive for nothing less than congruence with Catholic moral teaching, and we settle for nothing less than solid returns. Drawing from our knowledge and experience gained over decades of achievement in wealth management, we expect that our values aligned investment strategies will yield competitive returns.</p>
    <div class="abs about__rule"></div>
    <div class="abs brand-mark about__brand"><span class="brand-mark__square"></span>CORVELLA WEALTH ADVISORS</div>
    <p class="abs contact__label">contact us</p>
    <div class="abs contact__icons">
      <span><svg width="18" height="18" viewBox="0 0 24 24" fill="none" stroke="#fff" stroke-width="2"><path d="M5 3h4l2 5-3 2a12 12 0 0 0 6 6l2-3 5 2v4a2 2 0 0 1-2 2A17 17 0 0 1 3 5a2 2 0 0 1 2-2z"/></svg></span>
      <span><svg width="18" height="18" viewBox="0 0 24 24" fill="none" stroke="#fff" stroke-width="2"><rect x="3" y="5" width="18" height="14"/><path d="M3 6l9 7 9-7"/></svg></span>
      <span><svg width="18" height="18" viewBox="0 0 24 24" fill="none" stroke="#fff" stroke-width="1.8"><circle cx="12" cy="12" r="9"/><path d="M3 12h18M12 3c3 3 3 15 0 18M12 3c-3 3-3 15 0 18"/></svg></span>
    </div>
    <p class="abs contact__phone">800.555.0142</p>
    <p class="abs contact__email">info@corvellawealth.com</p>
    <p class="abs contact__web">www.Corvella wealth.com</p>
    <div class="abs contact__social"><span></span><span></span><span></span></div>
  </div>

  <div class="abs cover">
    <div class="abs cover__photo" role="img" aria-label="Photo: a family standing on a rocky cliff above a deep blue sea with a sailboat"></div>
    <div class="abs brand-mark cover__brand"><span class="brand-mark__square"></span>CORVELLA WEALTH ADVISORS</div>
    <h1>
      <span class="abs cover__line cover__line--1">Empowering Catholics</span>
      <span class="abs cover__line cover__line--2">to align their</span>
      <span class="abs cover__line cover__line--3">faith and finance</span>
    </h1>
    <p class="abs cover__tag">High-tech analysis unlike anything else!</p>
  </div>
</section>

<section class="spread spread--inner">
  <div class="abs benefits-band"></div>
  <p class="abs benefits__lead">When you put your confidence in Corvella wealth advisors℠,</p>
  <h2 class="abs benefits__head">You'll benefit<br>from:</h2>
  <div class="abs benefits__rule"></div>
  <div class="abs family-photo" role="img" aria-label="Photo: parents and a young child playing together on grass in warm sunlight"></div>

  <ul class="abs benefit-list">
    <li style="top:0"><b>01</b><span>Transparency in your investments' corporate activities</span></li>
    <li style="top:52px"><b>02</b><span>A comprehensive values-based planning process</span></li>
    <li style="top:104px"><b>03</b><span>Tech-smart portfolios that aim to manage your funds strategically and efficiently</span></li>
    <li style="top:170px"><b>04</b><span>Financial planning that can take into account your complete financial picture</span></li>
    <li style="top:236px"><b>05</b><span>The convenience of having all your accounts in one place</span></li>
    <li style="top:296px"><b>06</b><span>Working with a fiduciary that works in your best interest</span></li>
  </ul>

  <div class="abs brand-mark firm__brand"><span class="brand-mark__square"></span>CORVELLA</div>
  <p class="abs firm__lead">Our firm is steeped in tradition and rooted in our Faith, but our tactics are very much Digital Age deploying tomorrow's technology at the cutting edge.</p>
  <p class="abs firm__tech">Utilizing emerging capabilities enabled by artificial intelligence and coupled with years of usage of quantitative analytics, Corvella Wealth Advisors℠ is advanced in its technical capability.</p>

  <div class="abs steps">
    <div class="step step--index">
      <div class="step__art" style="top:44px" role="img" aria-label="Line illustration: a clipboard report with a pen and profile card"></div>
      <p class="step__title" style="top:136px">Get your trust and ledger index℠</p>
      <p class="step__text" style="top:174px">Input a few key pieces of data to unveil your score online or schedule an appointment with our team at no cost no obligation.</p>
    </div>
    <div class="step step--account">
      <div class="step__art" style="top:34px;height:80px" role="img" aria-label="Line illustration: a laptop screen with a cursor arrow"></div>
      <p class="step__title" style="top:132px">Open an account<br>with us</p>
      <p class="step__text" style="top:170px">Once you receive your score, upload and transfer your assets to your faith-based portfolio. Our people and technology aim to make it simple!</p>
    </div>
    <div class="step step--progress">
      <div class="step__art" style="top:24px;height:80px" role="img" aria-label="Line illustration: growth bars rising over 5, 10 and 15 years"></div>
      <p class="step__title" style="top:120px">Monitor your<br>progress</p>
      <p class="step__text" style="top:158px">We are here to help keep you on track – working to have your investments reflect your beliefs and meet a lifetime of financial goals.</p>
    </div>
  </div>

  <div class="abs baby-photo" role="img" aria-label="Photo: a father lifting a smiling baby into a bright blue sky"></div>
  <div class="abs faq faq--cost">
    <p class="faq__q">What does it cost to work with Corvella Wealth Advisors℠?</p>
    <p class="faq__a">The Trust and Ledger Index℠ is free of charge and has zero obligation. A prospective client can also speak with a Corvella advisor with no obligation or cost. If a person decides to work with us, they will receive an agreement to sign that outlines the advisory fee structure. Anyone can review our disclosure documents on our website at any time.</p>
  </div>
  <div class="abs faq faq--help">
    <p class="faq__q">What if I need help?</p>
    <p class="faq__a">Corvella's team of highly trained professionals is always just a click away. Your advisor will work with you to fully develop your financial plan in detail.</p>
  </div>
</section>

</body>
</html>
```